Branded Resources for OVARTe--Word, PPT, Newsletter Templates

Hi,
I hope you are well. I am hoping to get some pricing on branding a Word and PPT template and a Newsletter template. I've uploaded the original files for quick reference.

I was hoping for a full-color version and a black/grayscale version of the word and PPT template. Full color for the newsletter.

Thanks in advance for your quote and expected timeline for this project.

Thanks,
Belosa
Updates

Thank you for your submission and patience. I had a family emergency, and just getting back online. I will review the submissions. Thank you. Belosa

Industry/Entity Type

management consulting. Here's my website: https://ovarte-example.com/

Requirements
Must have
• The Word, PPT and Newsletter templates should reflect the logo assets listed below. Open to complementary colors that complement red/orange/golds
Nice to have
• Vibrancy, diversity, community

```html
<!DOCTYPE html>
<html lang="en">
<head>
<meta charset="utf-8">
<title>OVARTe Presentation Template</title>
<link rel="stylesheet" href="https://fonts.googleapis.com/css2?family=Montserrat:wght@400;600;700&family=Open+Sans:wght@400;600;700&display=swap">
<style>
  :root {
    --page: #dcdddf;
    --crimson: #8a1c1c;
    --rust: #b5501f;
    --amber: #c98a2a;
    --gold: #e2a431;
    --ochre: #c4912b;
    --sand: #d7b98a;
    --mist: #ededee;
    --stone: #b9b9bb;
    --ink: #4a4a4a;
    --white: #ffffff;
  }
  * { box-sizing: border-box; margin: 0; padding: 0; }
  html, body { width: 968px; height: 1200px; overflow: hidden; background: var(--page); }
  .canvas { position: relative; width: 968px; height: 1200px; }

  .cover-slide {
    position: absolute; left: 198px; top: 85px; width: 550px; height: 307px;
    background: linear-gradient(90deg, var(--crimson) 0%, #a4321d 25%, var(--rust) 48%, var(--amber) 75%, var(--gold) 100%);
    overflow: hidden;
    font-family: "Open Sans", sans-serif;
    color: var(--white);
  }
  .cover-slide .portrait {
    position: absolute; left: 240px; top: 0; width: 310px; height: 307px;
    background: radial-gradient(ellipse at 55% 45%, rgba(235,150,50,0.55) 0%, rgba(200,100,35,0.35) 45%, rgba(0,0,0,0) 75%);
  }
  .cover-slide .accent-bar { position: absolute; left: 26px; top: 0; width: 4px; height: 166px; background: var(--gold); }
  .cover-slide .brand-name {
    position: absolute; left: 39px; top: 100px;
    font-family: "Open Sans", sans-serif; font-weight: 400; font-size: 15px;
    letter-spacing: 0.5px; color: var(--white);
  }
  .cover-slide .tag-bar { position: absolute; left: 26px; top: 126px; width: 4px; height: 38px; background: var(--white); }
  .cover-slide .tagline {
    position: absolute; left: 39px; top: 128px; font-size: 8.4px; line-height: 12.6px; letter-spacing: 0.1px;
  }
  .cover-slide .project-title {
    position: absolute; left: 27px; top: 176px; font-family: "Montserrat", sans-serif;
    font-weight: 700; font-size: 35px; line-height: 36px; letter-spacing: 3px;
  }

  .slide-sorter { position: absolute; left: 0; top: 0; }
  .t-head { font-family: "Open Sans", sans-serif; font-size: 3.6px; fill: #555; text-anchor: middle; }
  .t-big { font-family: "Montserrat", sans-serif; font-weight: 700; fill: var(--white); }
  .t-body { font-family: "Open Sans", sans-serif; fill: var(--white); }
  .t-dark { font-family: "Open Sans", sans-serif; fill: #333; }
</style>
</head>
<body>
<div class="canvas">

  <section class="cover-slide">
    <div class="portrait" role="img" aria-label="Portrait photo of a smiling businesswoman resting her chin on her hand, toned orange"></div>
    <div class="accent-bar"></div>
    <div class="brand-name">OVARTe</div>
    <div class="tag-bar"></div>
    <p class="tagline">YOUR COMPANY – THE LARGEST<br>SUPLIER OF INTEGRATED<br>SOLUTIONS FOR INDUSTRIAL</p>
    <h1 class="project-title">PROJECT<br>TITLE</h1>
  </section>

  <svg class="slide-sorter" width="968" height="1200" viewBox="0 0 968 1200">
    <defs>
      <linearGradient id="band" x1="0" x2="1">
        <stop offset="0" stop-color="#e2a431"/><stop offset="1" stop-color="#8a1c1c"/>
      </linearGradient>
      <linearGradient id="cover" x1="0" x2="1">
        <stop offset="0" stop-color="#8a1c1c"/><stop offset="0.5" stop-color="#b5501f"/><stop offset="1" stop-color="#e2a431"/>
      </linearGradient>
      <linearGradient id="tan" x1="0" x2="1">
        <stop offset="0" stop-color="#d9b77a"/><stop offset="1" stop-color="#a88a5c"/>
      </linearGradient>
      <linearGradient id="grey" x1="0" x2="1">
        <stop offset="0" stop-color="#cfcfd1"/><stop offset="1" stop-color="#a9a9ab"/>
      </linearGradient>
      <g id="foot"><rect x="0" y="61.5" width="113" height="2.5" fill="url(#band)"/></g>
    </defs>

    <!-- Row 1 -->
    <g transform="translate(55,583)">
      <rect width="113" height="64" fill="url(#cover)"/>
      <rect x="58" width="55" height="64" fill="#e0a040" opacity="0.35" role="img" aria-label="Portrait photo of a businesswoman"/>
      <rect x="4" y="0" width="1" height="40" fill="#e2a431"/>
      <text x="8" y="24" class="t-body" font-size="3.2">OVARTe</text>
      <text x="8" y="39" class="t-big" font-size="6.5">PROJECT</text>
      <text x="8" y="46" class="t-big" font-size="6.5">TITLE</text>
    </g>
    <g transform="translate(179,583)">
      <rect width="113" height="64" fill="url(#tan)" role="img" aria-label="Photo of hands using a smartphone"/>
      <text x="108" y="5" class="t-body" font-size="3.6" text-anchor="end">Awesome Slide</text>
      <text x="9" y="23" class="t-body" font-size="5">You have to</text>
      <text x="9" y="29" class="t-body" font-size="5">step forwards</text>
      <text x="9" y="35" class="t-body" font-size="5">The future!</text>
    </g>
    <g transform="translate(304,583)">
      <rect width="113" height="64" fill="url(#grey)" role="img" aria-label="Photo of modern house architecture"/>
      <circle cx="33" cy="30" r="27" fill="#c96a2a" opacity="0.92"/>
      <text x="15" y="24" class="t-big" font-size="6">AWESOME</text>
      <text x="15" y="31" class="t-big" font-size="6">SLIDE</text>
    </g>
    <g transform="translate(428,583)">
      <rect width="113" height="64" fill="url(#tan)" role="img" aria-label="Photo of an audience at a conference"/>
      <text x="10" y="26" class="t-big" font-size="5.5">ANNUAL REPORT</text>
      <text x="10" y="33" class="t-big" font-size="5.5" fill="#e2a431">2018</text>
    </g>
    <g transform="translate(552,583)">
      <rect width="113" height="64" fill="url(#grey)" role="img" aria-label="Faded world map with crowd of people"/>
      <text x="56.5" y="6" class="t-head" fill="#fff">About Company</text>
      <g fill="#b5501f">
        <rect x="8" y="24" width="36" height="7" rx="3.5" transform="rotate(-35 26 27)"/>
        <rect x="10" y="34" width="36" height="7" rx="3.5" transform="rotate(-35 28 37)"/>
        <rect x="14" y="44" width="30" height="7" rx="3.5" transform="rotate(-35 29 47)"/>
      </g>
      <text x="16" y="32" class="t-big" font-size="6">WHO WE</text>
      <text x="18" y="39" class="t-big" font-size="6">ARE?</text>
      <text x="62" y="22" class="t-body" font-size="5">WHAT WE</text>
      <text x="62" y="28" class="t-body" font-size="5">DO</text>
    </g>
    <g transform="translate(677,583)">
      <rect width="113" height="64" fill="url(#grey)" role="img" aria-label="Faded world map with crowd of people"/>
      <text x="56.5" y="26" class="t-body" font-size="7" text-anchor="middle">WHO WE ARE?</text>
      <circle cx="18" cy="36" r="6" fill="none" stroke="#c96a2a" stroke-width="1.5"/>
      <circle cx="56" cy="44" r="6" fill="none" stroke="#e2a431" stroke-width="1.5"/>
      <circle cx="95" cy="36" r="6" fill="none" stroke="#c98a2a" stroke-width="1.5"/>
    </g>
    <g transform="translate(801,583)">
      <rect width="113" height="64" fill="url(#grey)" role="img" aria-label="Faded world map with crowd of people"/>
      <text x="56.5" y="6" class="t-head" fill="#fff">About Company</text>
      <rect x="0" y="17" width="72" height="18" fill="#c98a62" opacity="0.85"/>
      <text x="9" y="29" class="t-body" font-size="6.5">Lorem Ipsum</text>
      <line x1="60" y1="48" x2="90" y2="2" stroke="#222" stroke-width="1"/>
    </g>

    <!-- Row 2 -->
    <g transform="translate(55,658)">
      <rect width="113" height="64" fill="var(--mist)"/>
      <rect x="13" y="18" width="18" height="20" fill="#d4b5a4"/><rect x="13" y="38" width="18" height="18" fill="#b5501f"/>
      <rect x="36" y="18" width="18" height="20" fill="#c99fa3"/><rect x="36" y="38" width="18" height="18" fill="#8a1c1c"/>
      <rect x="59" y="18" width="18" height="20" fill="#dccba8"/><rect x="59" y="38" width="18" height="18" fill="#c4912b"/>
      <rect x="82" y="18" width="18" height="20" fill="#e9d7a6"/><rect x="82" y="38" width="18" height="18" fill="#e2a431"/>
      <use href="#foot"/>
    </g>
    <g transform="translate(179,658)">
      <rect width="113" height="64" fill="var(--mist)"/>
      <rect x="4" y="4" width="105" height="56" fill="#c4912b"/>
      <text x="56.5" y="20" class="t-body" font-size="5.5" text-anchor="middle">BIG</text>
      <text x="56.5" y="27" class="t-body" font-size="5.5" text-anchor="middle">PORTFOLIO</text>
      <text x="56.5" y="34" class="t-body" font-size="5.5" text-anchor="middle">SLIDE</text>
      <use href="#foot"/>
    </g>
    <g transform="translate(304,658)">
      <rect width="113" height="64" fill="#c98a62" role="img" aria-label="Photo of a smiling bearded man in glasses"/>
      <rect x="55" y="0" width="58" height="64" fill="#c4912b"/>
      <text x="8" y="20" class="t-body" font-size="5.5">Right</text>
      <text x="8" y="26" class="t-body" font-size="5.5">portfolio</text>
      <text x="8" y="32" class="t-body" font-size="5.5">slide</text>
      <text x="104" y="31" class="t-body" font-size="2.6" text-anchor="end">DESIGN IS NOT JUST</text>
      <text x="104" y="35" class="t-body" font-size="2.6" text-anchor="end">WHAT IT LOOKS LIKE</text>
    </g>
    <g transform="translate(428,658)">
      <rect width="113" height="64" fill="var(--white)"/>
      <rect width="56" height="64" fill="#c9a26a" role="img" aria-label="Photo of a woman reading documents"/>
      <g stroke="#3a7bd5" stroke-width="0.6" fill="none">
        <path d="M80 9 l1.5 1.5 l3 -3"/><path d="M80 23 l1.5 1.5 l3 -3"/><path d="M80 37 l1.5 1.5 l3 -3"/>
      </g>
      <use href="#foot"/>
    </g>
    <g transform="translate(552,658)">
      <rect width="113" height="64" fill="var(--white)"/>
      <text x="56.5" y="6" class="t-head">About Company</text>
      <text x="7" y="19" class="t-dark" font-size="3.8" font-weight="700">FEATURED</text>
      <text x="7" y="24" class="t-dark" font-size="3.8">WORK</text>
      <circle cx="10" cy="46" r="3" fill="#e2a431"/><circle cx="19" cy="46" r="3" fill="#c98a2a"/>
      <circle cx="28" cy="46" r="3" fill="#b5501f"/><circle cx="37" cy="46" r="3" fill="#8a1c1c"/>
      <g fill="none" stroke="#999" stroke-width="0.4">
        <rect x="58" y="18" width="18" height="18" transform="rotate(-10 67 27)"/>
        <rect x="74" y="14" width="18" height="18" transform="rotate(8 83 23)"/>
        <rect x="66" y="32" width="18" height="18" transform="rotate(5 75 41)"/>
        <rect x="84" y="34" width="18" height="18" transform="rotate(-12 93 43)"/>
      </g>
      <use href="#foot"/>
    </g>
    <g transform="translate(677,658)">
      <rect width="113" height="64" fill="var(--white)"/>
      <text x="56.5" y="6" class="t-head">About Company</text>
      <rect x="10" y="22" width="32" height="5" rx="2.5" fill="#e2a431"/>
      <rect x="10" y="31" width="45" height="5" rx="2.5" fill="#c4912b"/>
      <rect x="10" y="41" width="52" height="5" rx="2.5" fill="#8a1c1c"/>
      <text x="64" y="25" class="t-dark" font-size="3.5" font-weight="700">VELDARO</text>
      <circle cx="68" cy="50" r="2.5" fill="#e9d3a0"/><circle cx="76" cy="50" r="2.5" fill="#e9d3a0"/>
      <circle cx="84" cy="50" r="2.5" fill="#e2a431"/><circle cx="92" cy="50" r="2.5" fill="#e2a431"/>
      <use href="#foot"/>
    </g>
    <g transform="translate(801,658)">
      <rect width="113" height="64" fill="var(--white)"/>
      <text x="56.5" y="6" class="t-head">About Company</text>
      <path d="M45 33 L45 15 A18 18 0 0 1 61 25 Z" fill="#8a1c1c"/>
      <path d="M45 33 L61 25 A18 18 0 0 1 60 43 Z" fill="#b5501f"/>
      <path d="M45 33 L60 43 A18 18 0 1 1 45 15 Z" fill="#e2a431"/>
      <circle cx="90" cy="18" r="2" fill="#8a1c1c"/><circle cx="90" cy="28" r="2" fill="#e2a431"/>
      <circle cx="90" cy="38" r="2" fill="#c98a2a"/><circle cx="90" cy="48" r="2" fill="#e2a431"/>
      <use href="#foot"/>
    </g>

    <!-- Row 3 -->
    <g transform="translate(55,734)">
      <rect width="113" height="64" fill="var(--mist)"/>
      <rect x="9" y="22" width="5" height="28" rx="2" fill="#555" role="img" aria-label="Businessman silhouette"/>
      <rect x="99" y="22" width="5" height="28" rx="2" fill="#555" role="img" aria-label="Businesswoman silhouette"/>
      <rect x="36" y="22" width="48" height="4" rx="2" fill="#e2a431"/>
      <rect x="30" y="29" width="52" height="4" rx="2" fill="#8a1c1c"/>
      <rect x="24" y="36" width="58" height="4" rx="2" fill="#c4912b"/>
      <rect x="36" y="43" width="42" height="4" rx="2" fill="#b5501f"/>
      <use href="#foot"/>
    </g>
    <g transform="translate(179,734)">
      <rect width="113" height="64" fill="var(--white)"/>
      <text x="56.5" y="6" class="t-head">About Company</text>
      <g fill="#e2a431"><rect x="10" y="50" width="3" height="6"/><rect x="14" y="46" width="3" height="10"/><rect x="22" y="40" width="3" height="16"/><rect x="30" y="34" width="3" height="22"/><rect x="38" y="24" width="3" height="32"/></g>
      <g fill="#b5501f"><rect x="18" y="44" width="3" height="12"/><rect x="26" y="38" width="3" height="18"/><rect x="34" y="30" width="3" height="26"/></g>
      <rect x="42" y="18" width="3" height="38" fill="#8a1c1c"/>
      <use href="#foot"/>
    </g>
    <g transform="translate(304,734)">
      <rect width="113" height="64" fill="var(--white)"/>
      <text x="56.5" y="6" class="t-head">About Company</text>
      <circle cx="60" cy="31" r="11" fill="#8a1c1c"/>
      <circle cx="60" cy="31" r="13" fill="none" stroke="#ddd" stroke-width="0.8"/>
      <text x="60" y="33" class="t-big" font-size="5.5" text-anchor="middle">80%</text>
      <rect x="90" y="17" width="7" height="4" fill="#8a1c1c"/><rect x="90" y="25" width="7" height="4" fill="#b5501f"/>
      <rect x="90" y="33" width="7" height="4" fill="#c4912b"/><rect x="90" y="41" width="7" height="4" fill="#e2a431"/>
      <use href="#foot"/>
    </g>
    <g transform="translate(428,734)">
      <rect width="113" height="64" fill="var(--white)"/>
      <text x="56.5" y="6" class="t-head">About Company</text>
      <g fill="#c4912b"><rect x="20" y="22" width="3" height="20"/><rect x="32" y="24" width="3" height="18"/><rect x="60" y="18" width="3" height="24"/><rect x="72" y="22" width="3" height="20"/></g>
      <g fill="#e2a431"><rect x="24" y="18" width="3" height="24"/><rect x="64" y="20" width="3" height="22"/><rect x="84" y="24" width="3" height="18"/></g>
      <g fill="#8a1c1c"><rect x="28" y="26" width="3" height="16"/><rect x="40" y="28" width="3" height="14"/><rect x="68" y="26" width="3" height="16"/><rect x="88" y="26" width="3" height="16"/></g>
      <g fill="#b5501f"><rect x="36" y="20" width="3" height="22"/><rect x="48" y="24" width="3" height="18"/><rect x="76" y="24" width="3" height="18"/></g>
      <use href="#foot"/>
    </g>
    <g transform="translate(552,734)">
      <rect width="113" height="64" fill="var(--white)"/>
      <text x="56.5" y="6" class="t-head">About Company</text>
      <rect x="8" y="27" width="97" height="2" fill="#ddd"/>
      <circle cx="26" cy="28" r="5" fill="#e2a431"/><circle cx="36" cy="28" r="6" fill="#c4912b"/>
      <circle cx="50" cy="28" r="7" fill="#c98a2a"/><circle cx="66" cy="28" r="8" fill="#b5501f"/>
      <circle cx="85" cy="28" r="9" fill="#8a1c1c"/>
      <use href="#foot"/>
    </g>
    <g transform="translate(677,734)">
      <rect width="113" height="64" fill="var(--white)"/>
      <text x="56.5" y="6" class="t-head">About Company</text>
      <g stroke="#999" stroke-width="0.4" fill="none"><path d="M23 30 L38 20 M23 30 L38 40 M46 30 L67 30 M75 20 L90 30 M75 40 L90 30"/></g>
      <circle cx="23" cy="30" r="4" fill="#8a1c1c"/><circle cx="90" cy="30" r="4" fill="#8a1c1c"/>
      <circle cx="42" cy="30" r="3" fill="none" stroke="#888" stroke-width="0.4"/>
      <circle cx="71" cy="30" r="3" fill="none" stroke="#888" stroke-width="0.4"/>
      <circle cx="38" cy="18" r="3" fill="#e2a431"/><circle cx="75" cy="18" r="3" fill="#e2a431"/>
      <circle cx="38" cy="42" r="3" fill="#c4912b"/><circle cx="75" cy="42" r="3" fill="#c4912b"/>
      <use href="#foot"/>
    </g>
    <g transform="translate(801,734)">
      <rect width="113" height="64" fill="var(--white)"/>
      <text x="56.5" y="6" class="t-head">About Company</text>
      <circle cx="56" cy="30" r="11" fill="#e2a431"/>
      <circle cx="45" cy="20" r="5" fill="#e2a431"/><circle cx="67" cy="20" r="5" fill="#e2a431"/>
      <circle cx="44" cy="37" r="5" fill="#e2a431"/><circle cx="68" cy="37" r="5" fill="#e2a431"/>
      <circle cx="78" cy="28" r="3" fill="#bbb"/><circle cx="34" cy="28" r="3" fill="#bbb"/>
      <rect x="54" y="44" width="4" height="8" fill="#bbb"/>
      <use href="#foot"/>
    </g>

    <!-- Row 4 -->
    <g transform="translate(55,809)">
      <rect width="113" height="64" fill="var(--mist)"/>
      <path d="M8 17 H26 L31 30 L26 43 H8 Z" fill="#e2a431"/>
      <path d="M27 17 H44 L49 30 L44 43 H27 L32 30 Z" fill="#e9bb6a"/>
      <path d="M45 17 H62 L67 30 L62 43 H45 L50 30 Z" fill="#c4912b"/>
      <path d="M63 17 H80 L85 30 L80 43 H63 L68 30 Z" fill="#b5501f"/>
      <path d="M81 17 H98 L105 30 L98 43 H81 L86 30 Z" fill="#8a1c1c"/>
      <use href="#foot"/>
    </g>
    <g transform="translate(179,809)">
      <rect width="113" height="64" fill="var(--white)"/>
      <rect x="46" y="16" width="20" height="4" fill="#e2a431"/>
      <rect x="18" y="27" width="20" height="4" fill="#b5501f"/><rect x="46" y="27" width="20" height="4" fill="#b5501f"/><rect x="74" y="27" width="20" height="4" fill="#b5501f"/>
      <rect x="46" y="38" width="20" height="4" fill="#c4912b"/>
      <rect x="16" y="48" width="16" height="4" fill="#8a1c1c"/><rect x="36" y="48" width="16" height="4" fill="#8a1c1c"/>
      <rect x="58" y="48" width="16" height="4" fill="#8a1c1c"/><rect x="80" y="48" width="16" height="4" fill="#8a1c1c"/>
      <use href="#foot"/>
    </g>
    <g transform="translate(304,809)">
      <rect width="113" height="64" fill="var(--white)"/>
      <text x="56.5" y="6" class="t-head">About Company</text>
      <rect x="50" y="14" width="16" height="4" fill="#e2a431"/>
      <g fill="#8a1c1c"><rect x="16" y="24" width="14" height="4"/><rect x="34" y="24" width="14" height="4"/><rect x="20" y="33" width="14" height="4"/><rect x="20" y="41" width="14" height="4"/><rect x="20" y="49" width="14" height="4"/></g>
      <rect x="40" y="36" width="14" height="4" fill="#b5501f"/>
      <g fill="#c4912b"><rect x="56" y="24" width="14" height="4"/><rect x="68" y="33" width="14" height="4"/><rect x="62" y="43" width="14" height="4"/></g>
      <g fill="#e2a431"><rect x="80" y="24" width="14" height="4"/><rect x="84" y="38" width="14" height="4"/></g>
      <use href="#foot"/>
    </g>
    <g transform="translate(428,809)">
      <rect width="113" height="64" fill="var(--white)"/>
      <text x="56.5" y="6" class="t-head">About Company</text>
      <rect x="10" y="34" width="14" height="4" fill="#8a1c1c"/>
      <g fill="#b5501f"><rect x="32" y="26" width="14" height="4"/><rect x="32" y="34" width="14" height="4"/><rect x="32" y="42" width="14" height="4"/></g>
      <g fill="#c4912b"><rect x="52" y="20" width="14" height="4"/><rect x="52" y="28" width="14" height="4"/><rect x="52" y="36" width="14" height="4"/><rect x="52" y="44" width="14" height="4"/><rect x="72" y="20" width="14" height="4"/><rect x="72" y="36" width="14" height="4"/></g>
      <g fill="#e2a431"><rect x="92" y="20" width="14" height="4"/><rect x="92" y="30" width="14" height="4"/><rect x="92" y="40" width="14" height="4"/></g>
      <use href="#foot"/>
    </g>
    <g transform="translate(552,809)">
      <rect width="113" height="64" fill="var(--white)"/>
      <text x="56.5" y="6" class="t-head">About Company</text>
      <rect x="12" y="18" width="12" height="12" fill="#e2a431" transform="rotate(45 18 24)"/>
      <rect x="30" y="22" width="12" height="12" fill="#c4912b" transform="rotate(45 36 28)"/>
      <rect x="50" y="18" width="12" height="12" fill="#e2a431" transform="rotate(45 56 24)"/>
      <rect x="70" y="22" width="12" height="12" fill="#b5501f" transform="rotate(45 76 28)"/>
      <rect x="88" y="18" width="12" height="12" fill="#8a1c1c" transform="rotate(45 94 24)"/>
      <use href="#foot"/>
    </g>
    <g transform="translate(677,809)">
      <rect width="113" height="64" fill="var(--white)"/>
      <text x="56.5" y="6" class="t-head">About Company</text>
      <g stroke="#ccc" stroke-width="0.5"><line x1="16" y1="24" x2="16" y2="44"/><line x1="32" y1="28" x2="32" y2="44"/><line x1="48" y1="24" x2="48" y2="44"/><line x1="64" y1="28" x2="64" y2="44"/><line x1="80" y1="24" x2="80" y2="44"/><line x1="96" y1="22" x2="96" y2="44"/></g>
      <circle cx="16" cy="20" r="6" fill="#8a1c1c"/><circle cx="32" cy="26" r="4" fill="#e7a494"/>
      <circle cx="48" cy="22" r="5" fill="#b5501f"/><circle cx="64" cy="26" r="4" fill="#c4912b"/>
      <circle cx="80" cy="24" r="4" fill="#e9bb6a"/><circle cx="96" cy="20" r="6" fill="#e2a431"/>
      <use href="#foot"/>
    </g>
    <g transform="translate(801,809)">
      <rect width="113" height="64" fill="var(--white)"/>
      <text x="56.5" y="6" class="t-head">About Company</text>
      <rect x="10" y="31" width="92" height="2" fill="url(#band)"/>
      <g fill="none" stroke="#c98a2a" stroke-width="0.5">
        <circle cx="16" cy="20" r="3.5"/><circle cx="45" cy="20" r="3.5"/><circle cx="74" cy="20" r="3.5"/><circle cx="100" cy="20" r="3.5"/>
        <circle cx="30" cy="44" r="3.5"/><circle cx="60" cy="44" r="3.5"/><circle cx="88" cy="44" r="3.5"/>
      </g>
      <use href="#foot"/>
    </g>

    <!-- Row 5 -->
    <g transform="translate(55,884)">
      <rect width="113" height="64" fill="var(--mist)"/>
      <rect x="10" y="18" width="52" height="38" fill="#c46a3a" opacity="0.75" role="img" aria-label="Illustration of people figures in decreasing sizes"/>
      <use href="#foot"/>
    </g>
    <g transform="translate(179,884)">
      <rect width="113" height="64" fill="var(--mist)"/>
      <rect x="6" y="16" width="52" height="40" fill="#c98a2a" opacity="0.7" role="img" aria-label="Illustration of a team with idea bubbles"/>
      <use href="#foot"/>
    </g>
    <g transform="translate(304,884)">
      <rect width="113" height="64" fill="var(--mist)"/>
      <rect x="36" y="12" width="42" height="46" fill="#d79a3c" opacity="0.7" role="img" aria-label="Illustration of a person shaped as a tree"/>
      <use href="#foot"/>
    </g>
    <g transform="translate(428,884)">
      <rect width="113" height="64" fill="var(--mist)"/>
      <text x="56.5" y="6" class="t-head">About Company</text>
      <rect x="6" y="12" width="40" height="46" fill="#b5602e" opacity="0.7" role="img" aria-label="Illustration of a tree with icon bubbles"/>
      <circle cx="60" cy="38" r="3" fill="#e2a431"/><circle cx="74" cy="38" r="3" fill="#e2a431"/><circle cx="88" cy="38" r="3" fill="#e2a431"/>
      <use href="#foot"/>
    </g>
    <g transform="translate(552,884)">
      <rect width="113" height="64" fill="var(--mist)"/>
      <text x="56.5" y="6" class="t-head">About Company</text>
      <g fill="none" stroke="#b5501f" stroke-width="0.6"><circle cx="12" cy="24" r="3"/><circle cx="37" cy="24" r="3"/><circle cx="12" cy="44" r="3"/><circle cx="37" cy="44" r="3"/></g>
      <rect x="62" y="10" width="44" height="48" fill="#d38a34" opacity="0.7" role="img" aria-label="Illustration of a tree with a person"/>
      <use href="#foot"/>
    </g>
    <g transform="translate(677,884)">
      <rect width="113" height="64" fill="var(--white)"/>
      <text x="56.5" y="6" class="t-head">About Company</text>
      <path d="M10 56 V24 Q10 20 14 20 H66" fill="none" stroke="#8a1c1c" stroke-width="4"/>
      <path d="M18 56 V32 Q18 28 22 28 H60" fill="none" stroke="#b5501f" stroke-width="4"/>
      <path d="M26 56 V40 Q26 36 30 36 H54" fill="none" stroke="#c4912b" stroke-width="4"/>
      <path d="M34 56 V48 Q34 44 38 44 H48" fill="none" stroke="#e2a431" stroke-width="4"/>
      <use href="#foot"/>
    </g>
    <g transform="translate(801,884)">
      <rect width="113" height="64" fill="var(--white)"/>
      <text x="56.5" y="6" class="t-head">About Company</text>
      <path d="M14 38 Q24 22 34 34 T54 30 T74 34 T96 26" fill="none" stroke="#e2a431" stroke-width="1.5"/>
      <g fill="#fff" stroke="#c4912b" stroke-width="0.6"><circle cx="24" cy="31" r="4"/><circle cx="44" cy="33" r="4"/><circle cx="64" cy="30" r="4"/><circle cx="84" cy="31" r="4"/></g>
      <use href="#foot"/>
    </g>

    <!-- Row 6 -->
    <g transform="translate(55,960)">
      <rect width="113" height="64" fill="var(--white)"/>
      <path d="M10 18 H35 L38 22 L35 26 H10 Z" fill="#e2a431"/>
      <path d="M36 18 H60 L63 22 L60 26 H36 L39 22 Z" fill="#c98a2a"/>
      <path d="M61 18 H85 L88 22 L85 26 H61 L64 22 Z" fill="#b5501f"/>
      <path d="M86 18 H100 L105 22 L100 26 H86 L89 22 Z" fill="#8a1c1c"/>
      <circle cx="20" cy="36" r="3.5" fill="#e2a431"/><circle cx="44" cy="36" r="3.5" fill="#c98a2a"/>
      <circle cx="68" cy="36" r="3.5" fill="#b5501f"/><circle cx="92" cy="36" r="3.5" fill="#8a1c1c"/>
      <use href="#foot"/>
    </g>
    <g transform="translate(179,960)">
      <rect width="113" height="64" fill="var(--white)"/>
      <rect width="113" height="36" fill="#b5501f"/>
      <text x="24" y="18" class="t-body" font-size="4.2">CREATIVE</text>
      <text x="24" y="23" class="t-body" font-size="4.2">SAMPLE</text>
      <text x="24" y="28" class="t-body" font-size="4.2">TITLE</text>
      <circle cx="16" cy="46" r="3.5" fill="#e2a431"/><circle cx="46" cy="46" r="3.5" fill="#e2a431"/><circle cx="78" cy="46" r="3.5" fill="#e2a431"/>
      <use href="#foot"/>
    </g>
    <g transform="translate(304,960)">
      <rect width="113" height="64" fill="#b8b6b2" role="img" aria-label="Photo of a woman in yellow working on a laptop on a sofa"/>
      <use href="#foot"/>
    </g>
    <g transform="translate(428,960)">
      <rect width="113" height="64" fill="url(#grey)" role="img" aria-label="Faded city and network photo"/>
      <circle cx="28" cy="24" r="11" fill="#e2a431" opacity="0.8"/>
      <text x="48" y="20" class="t-body" font-size="3.4">WELCOME</text>
      <text x="48" y="25" class="t-body" font-size="3.6" font-weight="700">MESSAGE</text>
      <use href="#foot"/>
    </g>
    <g transform="translate(552,960)">
      <rect width="113" height="64" fill="var(--mist)"/>
      <rect width="113" height="36" fill="#a88a5c" role="img" aria-label="Photo of colleagues talking in an office"/>
      <circle cx="12" cy="46" r="3.5" fill="#8a1c1c"/><circle cx="46" cy="46" r="3.5" fill="#8a1c1c"/><circle cx="80" cy="46" r="3.5" fill="#8a1c1c"/>
      <use href="#foot"/>
    </g>
    <g transform="translate(677,960)">
      <rect width="113" height="64" fill="var(--mist)"/>
      <g stroke="#aaa" stroke-width="0.4"><path d="M57 33 L17 22 M57 33 L37 22 M57 33 L75 20 M57 33 L96 22 M57 33 L17 41 M57 33 L34 46 M57 33 L80 46 M57 33 L96 41"/></g>
      <circle cx="57" cy="33" r="7" fill="#8a1c1c"/>
      <circle cx="17" cy="22" r="4" fill="#c98a2a"/><circle cx="37" cy="22" r="4" fill="#b5501f"/>
      <circle cx="75" cy="20" r="4" fill="#b5501f"/><circle cx="96" cy="22" r="4" fill="#e2a431"/>
      <circle cx="17" cy="41" r="4" fill="#e2a431"/><circle cx="34" cy="46" r="4" fill="#e2a431"/>
      <circle cx="80" cy="46" r="4" fill="#b5501f"/><circle cx="96" cy="41" r="4" fill="#e2a431"/>
      <use href="#foot"/>
    </g>
    <g transform="translate(801,960)">
      <rect width="113" height="64" fill="var(--mist)"/>
      <circle cx="26" cy="38" r="12" fill="#f2d9a8"/><circle cx="50" cy="24" r="7" fill="#e9bb6a"/>
      <circle cx="56" cy="40" r="10" fill="#c4912b"/><circle cx="76" cy="22" r="6" fill="#e2a431"/>
      <circle cx="84" cy="40" r="9" fill="#8a1c1c"/>
      <use href="#foot"/>
    </g>

    <!-- Row 7 -->
    <g transform="translate(55,1035)">
      <rect width="113" height="64" fill="var(--mist)"/>
      <rect x="36" y="12" width="42" height="40" fill="#d38a34" opacity="0.7" role="img" aria-label="Illustration of a tree with hands"/>
      <rect x="30" y="54" width="6" height="4" fill="#e2a431"/><rect x="42" y="54" width="6" height="4" fill="#c4912b"/>
      <rect x="54" y="54" width="6" height="4" fill="#c98a2a"/><rect x="66" y="54" width="6" height="4" fill="#b5501f"/><rect x="78" y="54" width="6" height="4" fill="#8a1c1c"/>
      <use href="#foot"/>
    </g>
    <g transform="translate(179,1035)">
      <rect width="113" height="64" fill="var(--white)" stroke="#c4912b" stroke-width="0.5"/>
      <g fill="none" stroke="#c4912b" stroke-width="0.6">
        <path d="M32 32 H100 M52 32 V14 H100 M66 32 V24 H100 M52 32 V50 H100 M66 32 V40 H100"/>
        <circle cx="32" cy="32" r="2.5" fill="#fff"/><circle cx="52" cy="14" r="2.5" fill="#fff"/><circle cx="52" cy="50" r="2.5" fill="#fff"/>
      </g>
      <rect x="102" y="12" width="11" height="40" fill="url(#band)"/>
      <use href="#foot"/>
    </g>
    <g transform="translate(304,1035)">
      <rect width="113" height="64" fill="var(--white)"/>
      <text x="56.5" y="6" class="t-head">About Company</text>
      <circle cx="56" cy="33" r="13" fill="#e2a431"/><circle cx="56" cy="33" r="7" fill="#fff"/>
      <g fill="#fff" stroke="#c4912b" stroke-width="0.5"><circle cx="46" cy="19" r="3"/><circle cx="66" cy="19" r="3"/><circle cx="42" cy="33" r="3"/><circle cx="70" cy="33" r="3"/><circle cx="46" cy="47" r="3"/><circle cx="66" cy="47" r="3"/></g>
      <use href="#foot"/>
    </g>
    <g transform="translate(428,1035)">
      <rect width="113" height="64" fill="var(--mist)"/>
      <rect x="10" y="12" width="52" height="44" fill="#b5501f" opacity="0.7" role="img" aria-label="Illustration of speech bubbles above a hand"/>
      <use href="#foot"/>
    </g>
    <g transform="translate(552,1035)">
      <rect width="113" height="64" fill="var(--white)"/>
      <text x="56.5" y="6" class="t-head">About Company</text>
      <path d="M56 52 L34 52 A22 22 0 0 1 40 36 Z" fill="#e9bb6a"/>
      <path d="M56 52 L40 36 A22 22 0 0 1 56 30 Z" fill="#8a1c1c"/>
      <path d="M56 52 L56 30 A22 22 0 0 1 72 36 Z" fill="#c4912b"/>
      <path d="M56 52 L72 36 A22 22 0 0 1 78 52 Z" fill="#b5501f"/>
      <circle cx="56" cy="52" r="4" fill="#fff" stroke="#3a7bd5" stroke-width="0.5"/>
      <use href="#foot"/>
    </g>
    <g transform="translate(677,1035)">
      <rect width="113" height="64" fill="var(--white)"/>
      <text x="56.5" y="6" class="t-head">About Company</text>
      <rect x="12" y="17" width="3" height="3" fill="#c4912b"/><rect x="12" y="27" width="3" height="3" fill="#b5501f"/>
      <rect x="12" y="37" width="3" height="3" fill="#8a1c1c"/><rect x="12" y="47" width="3" height="3" fill="#8a1c1c"/>
      <circle cx="76" cy="33" r="11" fill="none" stroke="#e2a431" stroke-width="3"/>
      <path d="M76 22 A11 11 0 0 1 87 33" fill="none" stroke="#8a1c1c" stroke-width="3"/>
      <use href="#foot"/>
    </g>
    <g transform="translate(801,1035)">
      <rect width="113" height="64" fill="#bfb4a6" role="img" aria-label="Photo of a smiling diverse group of people"/>
      <rect x="0" y="38" width="113" height="26" fill="#e2a431"/>
    </g>

    <!-- Row 8 -->
    <g transform="translate(55,1110)">
      <rect width="113" height="64" fill="#f7f7f7"/>
      <g fill="none" stroke="#e2a431" stroke-width="1.4">
        <path d="M50 23 H62 V34 Q62 38 58 38 H54 Q50 38 50 34 Z" fill="#e2a431"/>
        <path d="M62 26 Q67 26 67 30 Q67 34 62 34"/>
        <path d="M55 14 Q53 17 56 19 M58 13 Q56 16 59 18" stroke-width="0.8"/>
      </g>
      <text x="56.5" y="46" class="t-dark" font-size="5" font-weight="700" text-anchor="middle">Break Slide</text>
      <use href="#foot"/>
    </g>
  </svg>

</div>
</body>
</html>
```